Name card design for KORU mobile accessories company

KORU is an upmarket brand, we are looking for professional business card design.

the design should be neat and simple but giving a strong feeling.
should not be colorful. make it black/white/gray tone

Name:
Job title:
Contact no.:
company address: i would like the company address to be very small and thin.
link to social media profile:
company website:

*the company have no website yet
as the project is done please i also would like the font that use in design as well; for more further people in company need a business card:)
Updates

Thank you for all super fast submission :D they're all look cool!

i have just update my brief to make the statement clearer, please check it out :)
if you have any question please dont hesitate to ask.
i would like see more design from you! 
Keep it up!  :D

Target Market(s)

Company target are upmarket company distributor, such as Velmora and Quill store.

Industry/Entity Type

Business

Font styles to use
Serif
Sans Serif
Other font styles liked:
• Formal and mordern

Colors
ffffff
eeeeee
d3d3d3
919191
474747
1b1b1b
000000
333333

Requirements
Must have
• The design must be professional clean and clear but also Strong and Modern!
text should be formal and mordern
Should not have
• No complicated design!

```html
<!DOCTYPE html>
<html lang="en">
<head>
<meta charset="utf-8">
<title>KORU Business Card</title>
<link href="https://fonts.googleapis.com/css2?family=Roboto+Condensed:wght@700&family=Roboto:wght@300;400;500&display=swap" rel="stylesheet">
<style>
  :root {
    --white: #ffffff;
    --paper: #eeeeee;
    --silver: #d3d3d3;
    --mid-gray: #919191;
    --dark-gray: #474747;
    --charcoal: #333333;
    --ink: #1b1b1b;
    --black: #000000;
  }
  * { margin: 0; padding: 0; box-sizing: border-box; }
  html, body { width: 1200px; height: 1000px; overflow: hidden; }
  body {
    background: var(--ink);
    font-family: "Roboto", sans-serif;
    position: relative;
  }
  .card {
    position: absolute;
    top: 350px;
    width: 520px;
    height: 300px;
    border-radius: 20px;
    background: linear-gradient(160deg, var(--white) 0%, var(--paper) 45%, var(--white) 62%, var(--silver) 100%);
    overflow: hidden;
  }
  .card-front { left: 50px; }
  .card-back { left: 630px; }
  .brand {
    display: flex;
    align-items: center;
    gap: 14px;
    color: var(--dark-gray);
    font-family: "Roboto Condensed", sans-serif;
    font-weight: 700;
    letter-spacing: 4px;
  }
  .brand-mark {
    background: var(--dark-gray);
    flex: none;
  }
  .card-front .brand {
    position: absolute;
    left: 50%; top: 50%;
    transform: translate(-50%, -50%);
    font-size: 76px;
  }
  .card-front .brand-mark { width: 26px; height: 26px; }
  .card-back .brand {
    position: absolute;
    left: 34px; top: 200px;
    font-size: 48px;
  }
  .card-back .brand-mark { width: 16px; height: 16px; }
  .divider {
    position: absolute;
    left: 236px; top: 60px;
    width: 1px; height: 220px;
    background: var(--mid-gray);
  }
  .details {
    position: absolute;
    left: 250px; top: 36px;
    color: var(--charcoal);
  }
  .name-first {
    font-family: "Roboto Condensed", sans-serif;
    font-weight: 700;
    font-size: 38px;
    line-height: 1;
    color: var(--charcoal);
  }
  .name-last {
    font-family: "Roboto Condensed", sans-serif;
    font-weight: 700;
    font-size: 22px;
    line-height: 1.1;
    color: var(--dark-gray);
  }
  .job-title {
    font-size: 10px;
    font-weight: 400;
    color: var(--mid-gray);
    margin-top: 2px;
  }
  .contact-list {
    list-style: none;
    margin-top: 26px;
  }
  .contact-item {
    display: flex;
    align-items: flex-start;
    gap: 10px;
    font-size: 10px;
    font-weight: 300;
    color: var(--dark-gray);
    line-height: 1.35;
    margin-bottom: 9px;
  }
  .contact-item svg { flex: none; width: 10px; height: 10px; margin-top: 2px; fill: var(--dark-gray); }
  .address { font-size: 9px; font-weight: 300; }
</style>
</head>
<body>
  <section class="card card-front">
    <div class="brand"><span class="brand-mark"></span>KORU</div>
  </section>

  <section class="card card-back">
    <div class="brand"><span class="brand-mark"></span>KORU</div>
    <div class="divider"></div>
    <div class="details">
      <div class="name-first">LARS</div>
      <div class="name-last">DEVOGHT</div>
      <div class="job-title">Vice President</div>
      <ul class="contact-list">
        <li class="contact-item address">
          <svg viewBox="0 0 10 10"><path d="M5 0a3.5 3.5 0 0 0-3.5 3.5C1.5 6 5 10 5 10s3.5-4 3.5-6.5A3.5 3.5 0 0 0 5 0zm0 5a1.5 1.5 0 1 1 0-3 1.5 1.5 0 0 1 0 3z"/></svg>
          <span>P.O. Box 20417, 00200 CPO<br>Lindvik, Norland</span>
        </li>
        <li class="contact-item">
          <svg viewBox="0 0 10 10"><path d="M2 0.5l1.6 2.2-1 1.1a6 6 0 0 0 3.6 3.6l1.1-1L9.5 8 8.3 9.5C4 9.5 0.5 6 0.5 1.7z"/></svg>
          <span>+31 555 60 18 42<br>+41 555 73 29 05</span>
        </li>
        <li class="contact-item">
          <svg viewBox="0 0 10 10"><path d="M0 2h10v6H0z M0 2l5 3.5L10 2" fill="none" stroke="#474747" stroke-width="1"/></svg>
          <span>lars@koru.co</span>
        </li>
        <li class="contact-item">
          <svg viewBox="0 0 10 10"><circle cx="5" cy="5" r="4.3" fill="none" stroke="#474747" stroke-width="1"/><path d="M0.7 5h8.6M5 0.7c-2.4 2.6-2.4 6 0 8.6M5 0.7c2.4 2.6 2.4 6 0 8.6" fill="none" stroke="#474747" stroke-width="0.8"/></svg>
          <span>www.koru.co</span>
        </li>
      </ul>
    </div>
  </section>
</body>
</html>
```